Business Card + Stationery Design for a Craft Beer Bar

Mr. Tovell's is a taproom sport bar that contains in its menu beers from different places around the world. What we offer differently is the experience that you can get inside our location, ambient music with rock from the 80s to 90s, projection with the sports of the moment, board games and private events.

Target Market(s)

Young people, Mid and High Class

Industry/Entity Type

Business

Font styles to use
Serif
Sans Serif

Colors
fee18a

Requirements
Must have
• Name, Title, Contact Details, Website
Nice to have
• Mail Signature
Should not have
• n/a

```html
<!DOCTYPE html>
<html lang="en">
<head>
<meta charset="utf-8">
<title>Mr. Tovell's Taproom – Business Card</title>
<link rel="stylesheet" href="https://fonts.googleapis.com/css2?family=Open+Sans:wdth,wght@75..100,400..700&display=swap">
<style>
  :root {
    --backdrop: #e9e6e1;
    --card-dark: #1f1a11;
    --card-yellow: #f4c257;
    --name-yellow: #f3b83c;
    --text-light: #f4f1ea;
    --seal-white: #f1f0ee;
    --seal-ink: #1c1a17;
  }
  * { margin: 0; padding: 0; box-sizing: border-box; }
  html, body {
    width: 1200px;
    height: 900px;
    overflow: hidden;
    background: var(--backdrop);
    font-family: "Open Sans", Arial, sans-serif;
  }
  .business-card {
    position: absolute;
    left: 190px;
    top: 197px;
    width: 820px;
    height: 506px;
    background: var(--card-dark);
    overflow: hidden;
    box-shadow: 0 12px 30px rgba(0, 0, 0, 0.18);
  }
  .accent-band {
    position: absolute;
    top: 0;
    right: 0;
    width: 272px;
    height: 100%;
    background: var(--card-yellow);
  }
  .brand-seal {
    position: absolute;
    left: 330px;
    top: 40px;
    width: 444px;
    height: 444px;
    border-radius: 50%;
    background: var(--seal-white);
  }
  .brand-name {
    position: absolute;
    left: 0;
    right: 0;
    top: 262px;
    text-align: center;
    font-weight: 600;
    font-size: 44px;
    line-height: 1;
    color: var(--seal-ink);
  }
  .identity {
    position: absolute;
    left: 44px;
    top: 80px;
  }
  .person-name {
    font-weight: 700;
    font-stretch: 78%;
    font-size: 36px;
    line-height: 1;
    color: var(--name-yellow);
    text-transform: uppercase;
  }
  .person-title {
    font-size: 20px;
    color: var(--text-light);
    margin-top: 4px;
  }
  .contact-list {
    position: absolute;
    left: 44px;
    top: 276px;
    list-style: none;
    font-size: 20px;
    color: var(--text-light);
  }
  .contact-list li {
    display: flex;
    align-items: center;
    height: 30px;
  }
  .contact-icon {
    width: 18px;
    height: 18px;
    margin-right: 8px;
    fill: var(--name-yellow);
  }
  .postal-address {
    position: absolute;
    left: 44px;
    top: 382px;
    font-style: normal;
    font-size: 20px;
    line-height: 30px;
    color: var(--text-light);
  }
</style>
</head>
<body>
  <section class="business-card">
    <div class="accent-band"></div>
    <div class="brand-seal">
      <span class="brand-name">Mr. Tovell's</span>
    </div>

    <header class="identity">
      <h1 class="person-name">Daniel Harlow</h1>
      <p class="person-title">Managing Director</p>
    </header>

    <ul class="contact-list">
      <li>
        <svg class="contact-icon" viewBox="0 0 24 24" aria-hidden="true"><path d="M6.6 10.8a15.2 15.2 0 0 0 6.6 6.6l2.2-2.2a1 1 0 0 1 1-.25 11.4 11.4 0 0 0 3.6.57 1 1 0 0 1 1 1V20a1 1 0 0 1-1 1A17 17 0 0 1 3 4a1 1 0 0 1 1-1h3.5a1 1 0 0 1 1 1c0 1.25.2 2.45.57 3.57a1 1 0 0 1-.25 1z"/></svg>
        (041)580 2736
      </li>
      <li>
        <svg class="contact-icon" viewBox="0 0 24 24" aria-hidden="true"><path d="M2 5h20v14H2z M3.5 6.5v1l8.5 5.5 8.5-5.5v-1z" fill-rule="evenodd"/></svg>
        hello@tovells.com
      </li>
      <li>
        <svg class="contact-icon" viewBox="0 0 24 24" aria-hidden="true"><path d="M12 2a10 10 0 1 0 0 20 10 10 0 0 0 0-20zm-1 17.9A8 8 0 0 1 4.1 11H7c.1 2.6.9 5.3 2.3 7.6zM4.1 10A8 8 0 0 1 11 4.1V10zm8-5.9a8 8 0 0 1 6.9 6.9H13zM13 12h6.9a8 8 0 0 1-6.9 6.9z"/></svg>
        www.tovellstap.com
      </li>
    </ul>

    <address class="postal-address">
      88 Harbour Lane,<br>
      Brightwater, 40218
    </address>
  </section>
</body>
</html>
```